Need Epic Web Banner for New Site

We need a banner for our web page. We are BrightStrydo.com, think of us as the Pondelly of the highest quality sports nutrition supplements on the web. Our site is under construction, if you visit our site, this banner will go at the very top above the menu bar. We are marketing supplements a different way then most; we are staying away from hulked out guys on steroids & gimmick magic pills/ slogans. We are all about clean quality products with less ingredients.

We are attaching our logo/ symbol & a text we made in AI for a point of reference. Please help us bring our site and vision of BrightStrydo to life!

We are not married to the colors but GREEN is a must!
Updates

Disregard previous message about Tova's entry. This platform does not allow me to delet comments I post.

Target Market(s)

Heath Consious, Health Seekers, Active Fit People, Gym Rats, Rock Climbers

Industry/Entity Type

Nutrition

Font styles to use
Other font styles liked:
• Semplicita

Colors
33b8a4
00a990
86cfc6

Requirements
Must have
• For text In addition to BrightStrydo.com we'd like "Not all supplements are created equal"

```html
<!DOCTYPE html>
<html lang="en">
<head>
<meta charset="utf-8">
<title>BrightStrydo.com – Web Banners</title>
<link rel="stylesheet" href="https://fonts.googleapis.com/css2?family=Oswald:wght@400;600&display=swap">
<style>
  :root {
    --page-bg: #ffffff;
    --green-deep: #00967f;
    --green-dark: #1f8f76;
    --green-mid: #33b8a4;
    --green-light: #6fcaa6;
    --green-pale: #86cfc6;
    --mint: #a9dcae;
    --figure-tone: #7fe0bd;
    --ink: #1c3b33;
    --white: #ffffff;
  }
  * { box-sizing: border-box; margin: 0; padding: 0; }
  html, body {
    width: 1200px;
    height: 694px;
    overflow: hidden;
    background: var(--page-bg);
  }
  .canvas {
    position: relative;
    width: 1200px;
    height: 694px;
  }
  .banner {
    position: absolute;
    overflow: hidden;
  }

  /* Banner one: emblem left, wordmark right */
  .banner--emblem {
    left: 26px;
    top: 43px;
    width: 1146px;
    height: 245px;
    background: linear-gradient(90deg, var(--green-dark) 0%, var(--green-mid) 25%, var(--green-light) 55%, var(--green-light) 75%, var(--green-dark) 100%);
  }
  .emblem-ring {
    position: absolute;
    left: 106px;
    top: -42px;
    width: 328px;
    height: 328px;
    border-radius: 50%;
    background: var(--green-deep);
    border: 3px solid var(--white);
    box-shadow: -4px 2px 0 #0b3b30;
  }
  .emblem-ring::after {
    content: "";
    position: absolute;
    left: 14px;
    top: 14px;
    width: 262px;
    height: 262px;
    border-radius: 50%;
    border: 3px solid var(--white);
  }
  .emblem-figures {
    position: absolute;
    left: 118px;
    top: 8px;
    width: 282px;
    height: 222px;
    border-radius: 40px 40px 10px 10px;
    background: linear-gradient(180deg, var(--figure-tone) 0%, #5cc9a3 100%);
  }
  .brand-block {
    position: absolute;
    right: 36px;
    top: 52px;
    text-align: right;
  }
  .brand-name {
    font-family: "Oswald", sans-serif;
    font-weight: 400;
    font-size: 58px;
    line-height: 1;
    letter-spacing: 1px;
    color: var(--ink);
  }
  .tagline {
    font-family: "Oswald", sans-serif;
    font-weight: 600;
    text-transform: uppercase;
    color: var(--white);
  }
  .banner--emblem .tagline {
    margin-top: 26px;
    font-size: 23px;
    letter-spacing: 0.3px;
  }

  /* Banner two: figures left, brand mark right */
  .banner--figures {
    left: 25px;
    top: 372px;
    width: 1151px;
    height: 246px;
    background: linear-gradient(90deg, var(--green-mid) 0%, #3cbc97 50%, var(--green-light) 100%);
  }
  .mark-glow {
    position: absolute;
    left: 780px;
    top: -40px;
    width: 340px;
    height: 330px;
    background: radial-gradient(circle, rgba(255,255,255,0.95) 0%, rgba(255,255,255,0.55) 30%, rgba(255,255,255,0) 65%);
  }
  .figures-art {
    position: absolute;
    left: 212px;
    top: 2px;
    width: 292px;
    height: 244px;
    border-radius: 60px 60px 0 0;
    background: linear-gradient(180deg, var(--figure-tone) 0%, #4fc39c 100%);
  }
  .tagline-bar {
    position: absolute;
    left: 0;
    top: 202px;
    width: 461px;
    height: 44px;
    background: var(--green-deep);
    border-top: 2px solid var(--white);
    padding-left: 13px;
    display: flex;
    align-items: center;
  }
  .banner--figures .tagline {
    font-size: 18px;
  }
  .brand-mark {
    position: absolute;
    left: 852px;
    top: 100px;
    display: flex;
    align-items: center;
    gap: 10px;
  }
  .brand-mark__dot {
    width: 40px;
    height: 40px;
    border-radius: 50%;
    background: var(--mint);
  }
  .brand-mark__name {
    font-family: "Oswald", sans-serif;
    font-weight: 400;
    font-size: 32px;
    color: var(--ink);
  }
</style>
</head>
<body>
<main class="canvas">

  <section class="banner banner--emblem" aria-label="Header banner with emblem">
    <div class="emblem-ring"></div>
    <div class="emblem-figures" role="img" aria-label="Illustration of a fit woman flexing her arm beside a muscular man"></div>
    <div class="brand-block">
      <p class="brand-name">BrightStrydo.com</p>
      <p class="tagline">Not all supplements are created equal</p>
    </div>
  </section>

  <section class="banner banner--figures" aria-label="Header banner with brand mark">
    <div class="mark-glow"></div>
    <div class="figures-art" role="img" aria-label="Illustration of a fit woman flexing her arm beside a muscular man"></div>
    <div class="tagline-bar">
      <p class="tagline">Not all supplements are created equal</p>
    </div>
    <div class="brand-mark">
      <span class="brand-mark__dot"></span>
      <span class="brand-mark__name">BrightStrydo</span>
    </div>
  </section>

</main>
</body>
</html>
```